Security Warning Sign

We have an existing sign that needs an update. I have attached a picture of the current square sign. We need to maintain the same wording. It needs to be professional and appropriate to attach to our customers fence. Also attached is a copy of our building sign which may lend some inspiration and hopefully the ai format will assist. The final sign will be 600mm x 600mmOur website is www.halvorngate.com.au

```html
<!DOCTYPE html>
<html lang="en">
<head>
<meta charset="utf-8">
<title>Warning Sign – Electronic Surveillance</title>
<link rel="stylesheet" href="https://fonts.googleapis.com/css2?family=Fira+Sans:wght@400;600;800;900&display=swap">
<style>
  :root {
    --orange: #ef8730;
    --white: #ffffff;
    --ink: #1a1a1a;
    --stripe-grey: #9a9a9a;
    --page: #ffffff;
  }
  html, body {
    margin: 0;
    padding: 0;
    width: 1200px;
    height: 785px;
    overflow: hidden;
    background: var(--page);
    font-family: "Fira Sans", Arial, sans-serif;
  }
  .canvas {
    position: relative;
    width: 1200px;
    height: 785px;
  }
  .sign {
    position: absolute;
    left: 270px;
    top: 62px;
    width: 652px;
    height: 653px;
    background: var(--orange);
  }
  .sign-title {
    position: absolute;
    left: 0;
    right: 0;
    top: 20px;
    margin: 0;
    text-align: center;
    color: var(--white);
    font-weight: 900;
    font-size: 118px;
    line-height: 1;
    letter-spacing: -2px;
  }
  .sign-panel {
    position: absolute;
    left: 13px;
    top: 176px;
    width: 625px;
    height: 462px;
    background: var(--white);
    overflow: hidden;
  }
  .notice {
    position: absolute;
    left: 55px;
    top: 22px;
    margin: 0;
    color: var(--ink);
    font-weight: 900;
    font-size: 77px;
    line-height: 72px;
    letter-spacing: 1px;
  }
  .notice-line { display: block; }
  .notice-sub {
    display: inline-block;
    vertical-align: 6px;
    margin-left: 14px;
    font-weight: 800;
    font-size: 28px;
    line-height: 26px;
    letter-spacing: 0;
  }
  .company {
    position: absolute;
    left: 48px;
    top: 258px;
    display: flex;
    align-items: center;
    gap: 14px;
  }
  .company-mark {
    width: 58px;
    height: 58px;
    border-radius: 50%;
    background: var(--orange);
  }
  .company-name {
    color: var(--ink);
    font-weight: 800;
    font-size: 23px;
    line-height: 24px;
    text-transform: uppercase;
  }
  .phone-band {
    position: absolute;
    left: 0;
    top: 350px;
    width: 320px;
    height: 62px;
  }
  .phone-band svg { position: absolute; left: 0; top: 0; }
  .phone {
    position: absolute;
    left: 55px;
    top: 10px;
    margin: 0;
    color: var(--white);
    font-weight: 800;
    font-size: 38px;
    line-height: 42px;
    letter-spacing: 0.5px;
  }
  .website {
    position: absolute;
    left: 58px;
    top: 424px;
    margin: 0;
    color: var(--ink);
    font-weight: 400;
    font-size: 24px;
    line-height: 28px;
  }
  .camera-art {
    position: absolute;
    left: 380px;
    top: 254px;
    width: 220px;
    height: 208px;
    background: linear-gradient(160deg, #2a2a2a, #111111);
    border-radius: 10px 10px 0 0;
  }
</style>
</head>
<body>
<div class="canvas">
  <section class="sign">
    <h1 class="sign-title">WARNING</h1>
    <div class="sign-panel">
      <p class="notice">
        <span class="notice-line">ELECTRONIC</span>
        <span class="notice-line">SURVEILLANCE</span>
        <span class="notice-line">DEVICES<span class="notice-sub">INSTALLED<br>IN THIS AREA</span></span>
      </p>

      <div class="company">
        <span class="company-mark"></span>
        <span class="company-name">Halvorngate<br>Security</span>
      </div>

      <div class="phone-band">
        <svg width="320" height="62" viewBox="0 0 320 62" aria-hidden="true">
          <polygon points="0,0 258,0 290,62 0,62" fill="var(--orange)"/>
          <polygon points="262,0 274,0 306,62 294,62" fill="var(--orange)"/>
          <polygon points="278,0 288,0 320,62 310,62" fill="var(--stripe-grey)"/>
        </svg>
        <p class="phone">1300 555 018</p>
      </div>

      <p class="website">halvorngate.com.au</p>

      <div class="camera-art" role="img" aria-label="Illustration of a wall-mounted security camera"></div>
    </div>
  </section>
</div>
</body>
</html>
```